Visitenkarten-Design für Maler
Zielgruppe
Ausführung von Malerarbeiten,Innenraumgestaltung
Aufgabenstellung
Stichworte :Eilaufträge Seniorenservice Kleinaufträge

```html
<!DOCTYPE html>
<html lang="de">
<head>
<meta charset="utf-8">
<title>Visitenkarte – Malerfachbetrieb Jonas Kellner</title>
<link rel="stylesheet" href="https://fonts.googleapis.com/css2?family=Lato:wght@400;700&display=swap">
<style>
  :root {
    --page-bg: #eeeeee;
    --card-white: #ffffff;
    --wash-blue: #3fb0e6;
    --wash-light: #a9dcf5;
    --wash-pale: #e6f5fc;
    --ink-grey: #5a5a5a;
    --ink-dark: #4a4a4a;
    --mark-red: #d9202a;
  }
  * { margin: 0; padding: 0; box-sizing: border-box; }
  html, body { width: 1200px; height: 864px; overflow: hidden; }
  body {
    background: var(--page-bg);
    font-family: "Lato", Arial, sans-serif;
    display: flex;
    align-items: center;
    justify-content: center;
    gap: 40px;
  }
  .card {
    position: relative;
    width: 520px;
    height: 336px;
    background: var(--card-white);
    overflow: hidden;
    box-shadow: 0 6px 18px rgba(0,0,0,0.12);
  }
  .wash {
    position: absolute;
    inset: 0;
  }
  .card--front .wash {
    background:
      radial-gradient(ellipse 60% 45% at 75% 85%, var(--wash-blue) 0%, transparent 70%),
      radial-gradient(ellipse 50% 40% at 15% 80%, var(--wash-light) 0%, transparent 75%),
      linear-gradient(170deg, var(--card-white) 0%, var(--card-white) 38%, var(--wash-pale) 55%, var(--wash-light) 80%, var(--wash-blue) 100%);
  }
  .card--back .wash {
    background:
      radial-gradient(ellipse 55% 20% at 55% 52%, var(--card-white) 0%, transparent 80%),
      radial-gradient(ellipse 50% 40% at 20% 10%, var(--wash-blue) 0%, transparent 75%),
      radial-gradient(ellipse 50% 40% at 85% 90%, var(--wash-blue) 0%, transparent 75%),
      linear-gradient(180deg, var(--wash-light) 0%, var(--wash-pale) 45%, var(--wash-pale) 58%, var(--wash-light) 100%);
  }
  .brand {
    position: absolute;
    left: 40px;
    top: 44px;
    display: flex;
    align-items: center;
    gap: 16px;
  }
  .brand__dot {
    width: 56px;
    height: 56px;
    border-radius: 50%;
    background: var(--mark-red);
    flex-shrink: 0;
  }
  .brand__name {
    color: var(--ink-dark);
    font-weight: 700;
    font-size: 26px;
    line-height: 1.1;
  }
  .services {
    position: absolute;
    left: 40px;
    top: 206px;
    color: var(--ink-dark);
    font-size: 16px;
    line-height: 1.6;
  }
  .contact {
    position: absolute;
    right: 34px;
    top: 120px;
    text-align: right;
    color: var(--ink-grey);
    font-size: 16px;
    line-height: 1.65;
  }
</style>
</head>
<body>
  <section class="card card--front">
    <div class="wash" role="img" aria-label="Hellblaue Aquarell-Textur, nach unten kräftiger werdend"></div>
    <div class="brand">
      <span class="brand__dot"></span>
      <p class="brand__name">Malerfachbetrieb<br>Jonas Kellner</p>
    </div>
    <div class="services">
      <p>Eilaufträge / Seniorenservice / Kleinaufträge</p>
      <p>Mobil: 0160/48236157</p>
    </div>
  </section>

  <section class="card card--back">
    <div class="wash" role="img" aria-label="Hellblaue Aquarell-Textur mit heller Wolkenzone in der Mitte"></div>
    <div class="contact">
      <p>Tel. 030/41872265</p>
      <p>www.malerbetrieb-jonas-kellner.de</p>
      <p>E-Mail: info@malerbetrieb-jonas-kellner.de</p>
    </div>
  </section>
</body>
</html>
```